General contractor/GM consaltant business card

I need a card for my contracting company in North Dakota, we build industrial buildings for the oil feild and oil feild related companies offices, shops, airplain hangars, airports ext. We have a familly atmosphere on the job and are very relational and personal.
Industry/Entity Type
Industrial
Contact Information for Business Card
Kestrelmoor Builders LLC.
Dwight T.Halvorsun
4736 Quillfern dr. Colorado Springs, CO. 80927
Cell# 406-555-8142
dwight@kestrelmoorbuilders.com

```html
<!DOCTYPE html>
<html lang="en">
<head>
<meta charset="utf-8">
<title>Kestrelmoor Builders LLC – Business Card</title>
<link rel="stylesheet" href="https://fonts.googleapis.com/css2?family=Arimo:wght@400;700&display=swap">
<style>
  :root {
    --brand-blue: #0019b0;
    --ink: #1a1a1a;
    --paper: #ffffff;
    --on-band: #ffffff;
  }
  html, body {
    margin: 0;
    padding: 0;
    width: 1200px;
    height: 686px;
    overflow: hidden;
    background: var(--paper);
  }
  .card {
    position: relative;
    width: 1200px;
    height: 686px;
    background: var(--paper);
    font-family: "Arimo", Arial, sans-serif;
    overflow: hidden;
  }
  .card-name {
    position: absolute;
    left: 71px;
    top: 118px;
    margin: 0;
    font-size: 53px;
    line-height: 1;
    font-weight: 700;
    letter-spacing: 4px;
    color: var(--brand-blue);
  }
  .contact-list {
    position: absolute;
    left: 71px;
    top: 368px;
    margin: 0;
    padding: 0;
    list-style: none;
    font-size: 25px;
    line-height: 41px;
    letter-spacing: 2.4px;
    color: var(--ink);
  }
  .contact-list li { height: 41px; margin-top: -8px; }
  .contact-list li:first-child { margin-top: 0; }
  .footer-band {
    position: absolute;
    left: 0;
    top: 546px;
    width: 1200px;
    height: 106px;
    background: var(--brand-blue);
    box-shadow: 0 -4px 6px rgba(0, 0, 0, 0.35);
  }
  .address {
    position: absolute;
    left: 71px;
    top: 14px;
    margin: 0;
    font-style: normal;
    font-size: 25px;
    line-height: 48px;
    letter-spacing: 2.4px;
    color: var(--on-band);
  }
  .company-name {
    position: absolute;
    left: 809px;
    top: 9px;
    margin: 0;
    font-size: 41px;
    line-height: 46px;
    font-weight: 700;
    letter-spacing: 3.5px;
    color: var(--on-band);
  }
</style>
</head>
<body>
  <main class="card">
    <h1 class="card-name">Dwight T.Halvorsun</h1>
    <ul class="contact-list">
      <li class="contact-phone">406-555-8142</li>
      <li class="contact-email">dwight@kestrelmoorbuilders.com</li>
      <li class="contact-web">www.kestrelmoorbuilders.com</li>
    </ul>
    <footer class="footer-band">
      <address class="address">4736 Quillfern dr. Colorado<br>Springs, CO. 80927</address>
      <p class="company-name">Kestrelmoor<br>Builders LLC</p>
    </footer>
  </main>
</body>
</html>
```